Business Card Design Project - Tall Maple

We are looking for a new business card design. Our company name is Tall Maple Communication Solutions. Our primary function is to provide our clients with communication solutions. These solutions include commercial phone systems and T1 and Fiber Internet lines. Another major part of the business is cabling new buildings with CAT5 cable for both data and phone.

Industry/Entity Type

Communication

Requirements
Must have
• The cards need to be two sided and have some bleeding edge color.
Nice to have
• We are going to upload our current logo BUT we are not married to this logo. If you want to incorporate a re-designed logo with the new business card - please feel free to do so. We are looking for a new bold look that is very colorful yet professional.

```html
<!DOCTYPE html>
<html lang="en">
<head>
<meta charset="utf-8">
<title>Tall Maple – Business Card</title>
<link rel="stylesheet" href="https://fonts.googleapis.com/css2?family=Source+Sans+3:wght@400;600;700&display=swap">
<style>
  :root {
    --page: #ffffff;
    --navy: #1d3f8c;
    --deep-blue: #1b3a88;
    --sky: #2aa6e0;
    --card-blue: #1a8fd6;
    --red: #d42a2f;
    --pink: #f2c7c9;
    --yellow: #fff200;
    --soft-text: #a9d6f3;
    --white: #ffffff;
  }
  * { box-sizing: border-box; margin: 0; padding: 0; }
  html, body {
    width: 1200px; height: 472px; overflow: hidden;
    background: var(--page);
    font-family: "Source Sans 3", Arial, sans-serif;
  }
  .stage { position: relative; width: 1200px; height: 472px; }
  .card {
    position: absolute; top: 66px;
    width: 520px; height: 376px;
    border-radius: 22px; overflow: hidden;
  }
  .card--front { left: 64px; background: var(--white); }
  .card--back { left: 630px; background: var(--card-blue); }

  .card__decor {
    position: absolute; top: 0; right: 0;
    width: 150px; height: 100%;
    background: linear-gradient(90deg, var(--yellow) 0%, var(--pink) 30%, var(--red) 55%, var(--sky) 100%);
    opacity: 0.85;
  }
  .card__decor--base {
    left: 0; right: auto; top: auto; bottom: 0;
    width: 100%; height: 34px;
    background: linear-gradient(90deg, var(--deep-blue), var(--sky));
    opacity: 1;
  }

  .brand {
    position: absolute; left: 0; top: 168px; width: 370px;
    text-align: center; color: var(--navy);
  }
  .brand__name { font-size: 34px; font-weight: 700; line-height: 1; }
  .brand__tagline {
    margin-top: 6px; font-size: 12px; font-weight: 700;
    letter-spacing: 1.6px; text-transform: uppercase;
  }

  .contact { position: absolute; left: 48px; top: 40px; color: var(--white); }
  .contact__name { font-size: 24px; font-weight: 700; line-height: 32px; margin-bottom: 20px; }
  .contact__lines { list-style: none; color: var(--soft-text); font-size: 15px; line-height: 20px; }
  .contact__address { margin-top: 14px; font-size: 15px; line-height: 21px; font-style: normal; }
</style>
</head>
<body>
<main class="stage">

  <section class="card card--front" aria-label="Card front">
    <div class="card__decor" role="img" aria-label="Curved colour bands in yellow, red and blue"></div>
    <div class="card__decor card__decor--base" role="img" aria-label="Dark-to-light blue sweep along the lower edge"></div>
    <div class="brand">
      <p class="brand__name">Tall Maple</p>
      <p class="brand__tagline">Communication Solutions</p>
    </div>
  </section>

  <section class="card card--back" aria-label="Card back">
    <div class="card__decor" role="img" aria-label="Curved colour bands in yellow, red and blue"></div>
    <div class="contact">
      <h1 class="contact__name">Owen Hartley</h1>
      <ul class="contact__lines">
        <li>Office: 602.555.0148</li>
        <li>Cell: 602.555.0193</li>
        <li>24/7: 800.555.0162</li>
        <li>Fax: 800.555.0177</li>
      </ul>
      <address class="contact__address">1840 W Desert Ridge Drive, Suite 400<br>Mesa, AZ 85201</address>
    </div>
  </section>

</main>
</body>
</html>
```